Glint5Gate Photography Business Cards

We need a good general business card that we can hand to our clients. We will be doing embossed gloss cards.

Target Market(s)

Real estate / Business to business / professionals

```html
<!DOCTYPE html>
<html lang="en">
<head>
<meta charset="utf-8">
<title>Glint5Gate Photography Business Cards</title>
<link href="https://fonts.googleapis.com/css2?family=PT+Sans:wght@400;700&display=swap" rel="stylesheet">
<style>
  :root {
    --navy: #231f63;
    --sky: #2a9fd8;
    --ink: #2b2b2b;
    --rule: #9a9a9a;
    --card: #ffffff;
    --emboss-light: #f4f4f5;
    --emboss-dark: #e6e6e8;
    --stage: #2a2a2b;
  }
  * { margin: 0; padding: 0; box-sizing: border-box; }
  html, body { width: 1200px; height: 1108px; overflow: hidden; }
  body {
    background: var(--stage);
    font-family: "PT Sans", Arial, sans-serif;
    position: relative;
  }
  .card {
    position: absolute;
    top: 169px;
    width: 440px;
    height: 770px;
    border-radius: 24px;
    background: var(--card);
    overflow: hidden;
  }
  .card--front { left: 130px; }
  .card--back { left: 630px; }

  .brand {
    position: absolute;
    top: 150px;
    left: 0;
    width: 100%;
    text-align: center;
    color: var(--navy);
    font-weight: 700;
    line-height: 1.05;
  }
  .brand__word { display: block; font-size: 58px; letter-spacing: 1px; }
  .brand__sub { display: block; font-size: 24px; letter-spacing: 9px; margin-top: 6px; }

  .person {
    position: absolute;
    top: 372px;
    left: 0;
    width: 100%;
    text-align: center;
  }
  .person__name { color: var(--navy); font-weight: 700; font-size: 30px; }
  .person__title { color: var(--sky); font-size: 18px; letter-spacing: 1px; margin-top: 2px; }

  .contact-icons {
    position: absolute;
    top: 456px;
    left: 60px;
    width: 320px;
    display: flex;
    align-items: center;
    gap: 8px;
  }
  .contact-icons__rule { flex: 1; height: 1px; background: var(--rule); }
  .contact-icons__item {
    width: 34px; height: 34px;
    background: var(--navy);
    border-radius: 5px;
    display: flex; align-items: center; justify-content: center;
  }

  .details {
    position: absolute;
    top: 510px;
    left: 0;
    width: 100%;
    text-align: center;
    color: var(--ink);
    font-size: 19px;
    line-height: 1.45;
  }
  .details__link { color: var(--sky); }
  .details__rule {
    width: 300px; height: 1px; background: var(--rule);
    margin: 14px auto 14px;
  }

  .emboss-field {
    position: absolute; inset: 0;
    background: radial-gradient(circle at 50% 50%, var(--emboss-light) 0%, var(--emboss-dark) 100%);
  }
  .back-mark {
    position: absolute;
    top: 0; left: 0; width: 100%; height: 100%;
    display: flex; flex-direction: column; align-items: center; justify-content: center;
    color: var(--navy);
    font-weight: 700;
    text-align: center;
    line-height: 1.05;
  }
  .back-mark__dot {
    width: 28px; height: 28px; border-radius: 50%;
    background: var(--navy);
    margin-bottom: 22px;
  }
  .back-mark__word { font-size: 52px; }
  .back-mark__sub { font-size: 22px; letter-spacing: 8px; margin-top: 8px; }
</style>
</head>
<body>
  <section class="card card--front">
    <div class="brand">
      <span class="brand__word">Glint5Gate</span>
      <span class="brand__sub">PHOTOGRAPHY</span>
    </div>

    <div class="person">
      <div class="person__name">Marcus Hale</div>
      <div class="person__title">MANAGING DIRECTOR</div>
    </div>

    <div class="contact-icons">
      <span class="contact-icons__rule"></span>
      <span class="contact-icons__item" aria-label="Phone">
        <svg width="20" height="20" viewBox="0 0 20 20"><path d="M4 3h4l1 4-2 1.5a10 10 0 0 0 4.5 4.5L13 11l4 1v4a1 1 0 0 1-1 1A14 14 0 0 1 3 4a1 1 0 0 1 1-1z" fill="#fff"/></svg>
      </span>
      <span class="contact-icons__item" aria-label="Mobile">
        <svg width="20" height="20" viewBox="0 0 20 20"><rect x="5" y="1.5" width="10" height="17" rx="2" fill="none" stroke="#fff" stroke-width="1.8"/><circle cx="10" cy="15.5" r="1" fill="#fff"/></svg>
      </span>
      <span class="contact-icons__item" aria-label="Email">
        <svg width="20" height="20" viewBox="0 0 20 20"><rect x="2" y="4.5" width="16" height="11" fill="none" stroke="#fff" stroke-width="1.6"/><path d="M2 4.5l8 6 8-6" fill="none" stroke="#fff" stroke-width="1.6"/></svg>
      </span>
      <span class="contact-icons__item" aria-label="Website">
        <svg width="20" height="20" viewBox="0 0 20 20"><circle cx="10" cy="10" r="7.5" fill="none" stroke="#fff" stroke-width="1.6"/><ellipse cx="10" cy="10" rx="3.2" ry="7.5" fill="none" stroke="#fff" stroke-width="1.3"/><path d="M2.5 10h15" stroke="#fff" stroke-width="1.3"/></svg>
      </span>
      <span class="contact-icons__rule"></span>
    </div>

    <div class="details">
      <div>044-310 275 864</div>
      <div>044-310 275 864</div>
      <div>hello@glint5gate.com</div>
      <div>www.<span class="details__link">glint5gate</span>.com</div>
      <div class="details__rule"></div>
      <div>88, Harbor Lane North</div>
      <div>45120, Eastland</div>
    </div>
  </section>

  <section class="card card--back">
    <div class="emboss-field" role="img" aria-label="Embossed repeating pattern of small camera and house motifs across the card"></div>
    <div class="back-mark">
      <span class="back-mark__dot"></span>
      <span class="back-mark__word">Glint5Gate</span>
      <span class="back-mark__sub">PHOTOGRAPHY</span>
    </div>
  </section>
</body>
</html>
```